Check, Perfect and Polish my Perfume Brochure

I will send my brochure to stores that sell perfumes.
The perfumes stores are located all around the world.

In this brochure/booklet I will tell the stores about my
1. my life
2. How I made perfumes on my own
3. I will talk about the perfumes I sell

I will use this brochure/booklet to make connections with perfume stores.
They should know, and remember who I am from this booklet.
I will use this brochure/booklet to make sales.

I need a graphic designer with
1. print experience
2. booklet and brochure making experience
3. very detailed eyes
4. good spelling
5. experience in fashion, health beauty products is important
6. please help me edit and polishing my brochure
7. my brochure to look very professional

This is the main point, to help me make my brochure look very cool, fashionable and professional

Target Market(s)

Perfume Store

Industry/Entity Type

perfumery, fashion, boutiques, high end luxury

Font styles to use
Serif

Colors
FFC000
F8CF3A
FAE287
FDF2CF
FEFAEE

Requirements
Must have
• 1. consistent design on all pages 2. have consistent colour and fonts 3. attractive photos 4. tell the stores about my brand 5. tell the stores about my life 6. tell the stores why my perfumes are very good
Nice to have
• I will like to have your personal style and suggestions please

```html
<!DOCTYPE html>
<html lang="en">
<head>
<meta charset="utf-8">
<title>About Me – Daniel James Hartley</title>
<link rel="stylesheet" href="https://fonts.googleapis.com/css2?family=Playfair+Display:wght@400;900&family=Roboto:wght@400;500&display=swap">
<style>
  :root {
    --gold: #ffc000;
    --gold-warm: #f8cf3a;
    --gold-soft: #fae287;
    --cream: #fdf2cf;
    --ivory: #fefaee;
    --ink: #111111;
    --photo-dark: #2c2d30;
    --photo-warm: #b58a4a;
    --photo-light: #d9d2c4;
  }
  * { margin: 0; padding: 0; box-sizing: border-box; }
  html, body { width: 1200px; height: 675px; overflow: hidden; background: var(--ivory); }
  .page {
    position: relative;
    width: 1200px;
    height: 675px;
    background: var(--ivory);
    color: var(--ink);
    font-family: "Roboto", Arial, sans-serif;
    overflow: hidden;
  }
  .header-band { position: absolute; left: 0; top: 0; width: 1200px; height: 215px; }
  .page-title {
    position: absolute;
    left: 0; right: 0;
    top: 80px;
    text-align: center;
    font-family: "Playfair Display", Georgia, serif;
    font-weight: 400;
    font-size: 90px;
    line-height: 1;
    letter-spacing: 1px;
    color: var(--ink);
  }
  .portrait-frame {
    position: absolute;
    left: 53px; top: 239px;
    width: 339px; height: 345px;
    background: var(--cream);
  }
  .portrait {
    position: absolute;
    left: 9px; top: 12px;
    width: 321px; height: 321px;
    background:
      radial-gradient(circle at 40% 75%, var(--photo-warm) 0%, rgba(181,138,74,0) 45%),
      linear-gradient(100deg, var(--photo-dark) 0%, #4a4a4e 45%, #8d8a85 70%, var(--photo-light) 100%);
  }
  .profile { position: absolute; left: 437px; top: 243px; }
  .profile-name {
    font-family: "Playfair Display", Georgia, serif;
    font-weight: 900;
    font-size: 41px;
    line-height: 1.1;
    letter-spacing: 0.2px;
  }
  .profile-roles {
    margin-top: 1px;
    font-weight: 500;
    font-size: 19.5px;
    line-height: 1.2;
  }
  .profile-roles .divider { margin: 0 14px; color: var(--gold); }
  .timeline { list-style: none; position: absolute; left: 437px; top: 325px; }
  .timeline li {
    display: flex;
    align-items: center;
    height: 41.3px;
    font-size: 24px;
    font-weight: 400;
    white-space: nowrap;
  }
  .timeline strong { font-weight: 500; }
  .timeline .marker { width: 17px; height: 17px; margin-right: 11px; flex: none; }
  .footer {
    position: absolute;
    left: 53px; right: 55px;
    top: 630px;
    display: flex;
    justify-content: space-between;
    font-weight: 500;
    font-size: 19.5px;
  }
</style>
</head>
<body>
<main class="page">
  <svg class="header-band" viewBox="0 0 1200 215" role="img" aria-label="Gold header band with a line-drawn floral pattern">
    <defs>
      <linearGradient id="bandFill" x1="0" y1="0" x2="1" y2="1">
        <stop offset="0" stop-color="var(--gold)"/>
        <stop offset="1" stop-color="var(--gold-warm)"/>
      </linearGradient>
    </defs>
    <path fill="url(#bandFill)" d="M0,0 H1200 V205 Q1185,198 1170,205 T1140,205 T1110,205 T1080,205 T1050,205 T1020,205 T990,205 T960,205 T930,205 T900,205 T870,205 T840,205 T810,205 T780,205 T750,205 T720,205 T690,205 T660,205 T630,205 T600,205 T570,205 T540,205 T510,205 T480,205 T450,205 T420,205 T390,205 T360,205 T330,205 T300,205 T270,205 T240,205 T210,205 T180,205 T150,205 T120,205 T90,205 T60,205 T30,205 T0,205 Z"/>
  </svg>
  <h1 class="page-title">ABOUT ME</h1>

  <div class="portrait-frame">
    <div class="portrait" role="img" aria-label="Portrait of the perfumer in an embroidered jacket, standing in a city alley"></div>
  </div>

  <section class="profile">
    <h2 class="profile-name">DANIEL JAMES HARTLEY</h2>
    <p class="profile-roles">Self-Educated Perfumer<span class="divider">I</span>Advocate for mental health</p>
  </section>

  <ul class="timeline">
    <li><svg class="marker" viewBox="0 0 20 20"><circle cx="10" cy="10" r="9" fill="none" stroke="var(--ink)" stroke-width="1.6"/><path d="M10 3.5 L16.5 10 L10 16.5 L3.5 10 Z" fill="var(--gold)"/><path d="M6.75 6.75 L13.25 13.25 M13.25 6.75 L6.75 13.25" stroke="var(--ink)" stroke-width="1.3"/></svg><span><strong>Born 1979</strong> : Managed family orchard to age 25</span></li>
    <li><svg class="marker" viewBox="0 0 20 20"><circle cx="10" cy="10" r="9" fill="none" stroke="var(--ink)" stroke-width="1.6"/><path d="M10 3.5 L16.5 10 L10 16.5 L3.5 10 Z" fill="var(--gold)"/><path d="M6.75 6.75 L13.25 13.25 M13.25 6.75 L6.75 13.25" stroke="var(--ink)" stroke-width="1.3"/></svg><span><strong>Education</strong> : Graphic Design &amp; Culinary Arts</span></li>
    <li><svg class="marker" viewBox="0 0 20 20"><circle cx="10" cy="10" r="9" fill="none" stroke="var(--ink)" stroke-width="1.6"/><path d="M10 3.5 L16.5 10 L10 16.5 L3.5 10 Z" fill="var(--gold)"/><path d="M6.75 6.75 L13.25 13.25 M13.25 6.75 L6.75 13.25" stroke="var(--ink)" stroke-width="1.3"/></svg><span><strong>2005 - 2015</strong> : Tokyo, Kyoto student to Japanese artisans</span></li>
    <li><svg class="marker" viewBox="0 0 20 20"><circle cx="10" cy="10" r="9" fill="none" stroke="var(--ink)" stroke-width="1.6"/><path d="M10 3.5 L16.5 10 L10 16.5 L3.5 10 Z" fill="var(--gold)"/><path d="M6.75 6.75 L13.25 13.25 M13.25 6.75 L6.75 13.25" stroke="var(--ink)" stroke-width="1.3"/></svg><span><strong>2015</strong> : Return to Canada</span></li>
    <li><svg class="marker" viewBox="0 0 20 20"><circle cx="10" cy="10" r="9" fill="none" stroke="var(--ink)" stroke-width="1.6"/><path d="M10 3.5 L16.5 10 L10 16.5 L3.5 10 Z" fill="var(--gold)"/><path d="M6.75 6.75 L13.25 13.25 M13.25 6.75 L6.75 13.25" stroke="var(--ink)" stroke-width="1.3"/></svg><span><strong>2015 - 2019</strong> : Self-Study Perfumery</span></li>
    <li><svg class="marker" viewBox="0 0 20 20"><circle cx="10" cy="10" r="9" fill="none" stroke="var(--ink)" stroke-width="1.6"/><path d="M10 3.5 L16.5 10 L10 16.5 L3.5 10 Z" fill="var(--gold)"/><path d="M6.75 6.75 L13.25 13.25 M13.25 6.75 L6.75 13.25" stroke="var(--ink)" stroke-width="1.3"/></svg><span><strong>December 2019</strong> : Release “Amber Fox Chypre”</span></li>
  </ul>

  <footer class="footer">
    <span class="footer-web">www.aurelscents.com</span>
    <span class="footer-contact">Perfumer@aurelscents.com I 1-555-014-2290</span>
  </footer>
</main>
</body>
</html>
```